KTW Ledgerwise Office Services Pty Ltd

Design a website for bookkeeping & accounting company

I like this website as an example with my own branding

https://go.quillcount.example/sydney-bookkeeping-lp/?keyword=bookkeeping%20sydney&matchtype=e&campaignid=482913057&device=c&adgroupid=31852064917&adposition=1t1&creative=607314928150&gclid=XkPwQrTbLmN3vZ8yHs5cDf2GaJ_uE0oWnRiYtBpKqLzMvXs_TeC

Number of Pages Required

1 page

Font styles to use
Sans Serif

Colors
9bcb3c

```html
<!DOCTYPE html>
<html lang="en">
<head>
<meta charset="utf-8">
<title>KTW Ledgerwise Office Services Pty Ltd</title>
<link rel="stylesheet" href="https://fonts.googleapis.com/css2?family=Montserrat:wght@400;500;600;700&family=Open+Sans:wght@400;600&display=swap">
<style>
:root{
  --green:#7fc242;
  --green-dark:#3c9a3a;
  --brand:#9bcb3c;
  --navy:#1f4f8a;
  --ink:#1d1d1d;
  --body:#444;
  --muted:#666;
  --line:#b9b9b9;
  --band:#f2f2f2;
  --footer:#0b0b0b;
  --white:#fff;
}
*{box-sizing:border-box;margin:0;padding:0}
html,body{width:1200px;height:3797px;overflow:hidden}
body{position:relative;background:var(--white);font-family:'Open Sans',Arial,sans-serif;color:var(--body)}
.abs{position:absolute}
h1,h2,h3,h4{font-family:'Montserrat',Arial,sans-serif;font-weight:500;color:var(--ink)}
.section-title{position:absolute;left:0;width:1200px;text-align:center;font-size:38px}

/* hero */
.hero{position:absolute;left:0;top:0;width:1200px;height:720px}
.brand-name{position:absolute;left:88px;top:46px;font-family:'Montserrat',Arial,sans-serif;font-weight:600;font-size:20px;color:var(--white);letter-spacing:.3px}
.topbar{position:absolute;left:876px;top:34px;font-family:'Montserrat',Arial,sans-serif;font-size:18px;color:var(--white);display:flex;gap:14px;align-items:center}
.topbar svg{width:14px;height:14px;margin-right:5px;vertical-align:-1px}
.nav{position:absolute;top:78px;left:616px;display:flex;gap:0;font-family:'Montserrat',Arial,sans-serif;font-size:18px;color:var(--white)}
.nav a{color:inherit;text-decoration:none;position:absolute;white-space:nowrap}
.nav a.active{color:var(--green)}
.hero-title{position:absolute;left:86px;top:322px;font-size:50px;line-height:72px;font-weight:600;color:var(--white)}

.quick-contact{position:absolute;left:775px;top:286px;width:336px;height:486px;background:var(--white);box-shadow:0 6px 20px rgba(0,0,0,.18);border-bottom:10px solid var(--green-dark)}
.quick-contact::before{content:"";position:absolute;left:0;top:30px;width:4px;height:40px;background:var(--navy)}
.quick-contact h3{position:absolute;top:30px;width:100%;text-align:center;font-size:24px}
.field{position:absolute;left:35px;width:263px;height:40px;border:2px solid var(--line);border-radius:20px;font-size:14px;color:var(--ink);padding:9px 18px}
.submit{position:absolute;left:86px;top:392px;width:152px;height:40px;border-radius:20px;background:linear-gradient(90deg,#1e4f8c,#2e9a4d);color:var(--white);font-family:'Montserrat',Arial,sans-serif;font-weight:700;font-size:16px;text-align:center;line-height:40px;box-shadow:0 4px 8px rgba(0,0,0,.25)}

/* services */
.service{position:absolute;width:300px;text-align:center}
.service .icon{width:112px;height:112px;margin:0 auto;border-radius:50%;border:3px solid var(--green-dark);display:flex;align-items:center;justify-content:center;box-shadow:0 3px 8px rgba(0,0,0,.15)}
.service h4{margin-top:40px;font-size:20px;font-weight:600}
.service p{margin:18px auto 0;width:230px;font-size:15px;line-height:26px}

/* about */
.about-band{position:absolute;left:0;top:1405px;width:1200px;height:436px;background:var(--band)}
.about-kicker{position:absolute;left:603px;top:1478px;font-family:'Montserrat',Arial,sans-serif;font-size:23px;color:var(--green-dark)}
.about-title{position:absolute;left:603px;top:1516px;font-size:30px;font-weight:400}
.about-text{position:absolute;left:603px;top:1560px;width:508px;font-size:14.5px;line-height:28px;color:var(--body)}
.pill-btn{position:absolute;height:30px;border-radius:15px;background:linear-gradient(90deg,#1e4f8c,#2e9a4d);color:var(--white);font-size:13px;text-align:center;line-height:30px;box-shadow:0 3px 6px rgba(0,0,0,.25)}

/* who we are */
.team-card{position:absolute;top:2066px;width:311px;height:352px;background:var(--white);box-shadow:0 2px 10px rgba(0,0,0,.18);text-align:center}
.team-card .photo{height:182px}
.team-card h4{margin-top:48px;font-size:18px;font-weight:500}
.team-card p{margin:12px auto 0;width:250px;font-size:12px;line-height:20px;color:var(--muted)}
.team-card .more{margin-top:8px;font-size:12px;color:var(--navy)}

/* stats */
.stats{position:absolute;left:0;top:2524px;width:1200px;height:408px;background:linear-gradient(100deg,#1d4f86 0%,#1f5a8a 40%,#2b7f62 75%,#3f9c45 100%)}
.stats h2{position:absolute;top:78px;width:100%;text-align:center;color:var(--white);font-size:38px;font-weight:400}
.stat{position:absolute;top:208px;width:240px;text-align:center;color:var(--white)}
.stat b{display:block;font-family:'Montserrat',Arial,sans-serif;font-weight:600;font-size:42px;line-height:50px}
.stat span{font-family:'Montserrat',Arial,sans-serif;font-size:20px}

/* blog */
.blog-card{position:absolute;top:3147px;width:498px;height:223px;border-radius:10px;overflow:hidden;box-shadow:0 2px 8px rgba(0,0,0,.2)}
.blog-caption{position:absolute;left:0;top:127px;width:278px;height:68px;background:rgba(255,255,255,.85);border-radius:0 12px 12px 0;padding:12px 20px}
.blog-caption h4{font-family:'Open Sans',Arial,sans-serif;font-size:17px;font-weight:400;color:var(--ink)}
.blog-caption span{font-size:13px;color:var(--green-dark)}
.view-more{position:absolute;left:1013px;top:3396px;font-size:14px;color:var(--navy);text-decoration:underline}

/* footer */
.footer{position:absolute;left:0;top:3500px;width:1200px;height:297px}
.footer-name{position:absolute;left:0;top:3612px;width:1200px;text-align:center;font-family:'Montserrat',Arial,sans-serif;font-weight:600;font-size:20px;color:var(--white)}
.socials{position:absolute;left:104px;top:3697px;display:flex;gap:12px}
.socials i{width:32px;height:32px;border:2px solid var(--white);border-radius:50%;display:block}
.copyright{position:absolute;left:866px;top:3697px;font-size:14px;color:var(--white)}
</style>
</head>
<body>

<!-- Hero -->
<svg class="hero" viewBox="0 0 1200 720" role="img" aria-label="Dark office photo of a person working with documents, a calculator and a laptop">
  <defs>
    <linearGradient id="heroShade" x1="0" y1="0" x2="1" y2="1">
      <stop offset="0" stop-color="#2b2b2b"/>
      <stop offset=".55" stop-color="#3a3c3d"/>
      <stop offset="1" stop-color="#1c1c1c"/>
    </linearGradient>
  </defs>
  <rect width="1200" height="720" fill="url(#heroShade)"/>
  <path d="M0 575 C 300 700 620 720 1200 560 L1200 720 L0 720 Z" fill="var(--green)"/>
  <path d="M0 620 C 300 710 620 730 1200 590 L1200 720 L0 720 Z" fill="#fff"/>
</svg>

<div class="brand-name">KTW Ledgerwise Office Services Pty Ltd</div>
<div class="topbar">
  <span><svg viewBox="0 0 24 24" fill="#fff"><path d="M6.6 10.8a15.1 15.1 0 0 0 6.6 6.6l2.2-2.2c.3-.3.7-.4 1-.2 1.1.4 2.3.6 3.6.6.6 0 1 .4 1 1V20c0 .6-.4 1-1 1A17 17 0 0 1 3 4c0-.6.4-1 1-1h3.5c.6 0 1 .4 1 1 0 1.3.2 2.5.6 3.6.1.3 0 .7-.2 1z"/></svg>080-41207356</span>
  <span>|</span>
  <span>LOGIN</span>
</div>
<nav class="nav">
  <a class="active" style="left:0">Home</a>
  <a style="left:95px">About us</a>
  <a style="left:214px">Services</a>
  <a style="left:321px">Blog</a>
  <a style="left:394px">Contact us</a>
</nav>
<h1 class="hero-title">We are a bookkeeping &amp;<br>accounting company.</h1>

<form class="quick-contact">
  <h3>Quick Contact</h3>
  <div class="field" style="top:100px">Name</div>
  <div class="field" style="top:156px">Email Id</div>
  <div class="field" style="top:212px">Phone</div>
  <div class="field" style="top:267px">Business Name</div>
  <div class="field" style="top:323px">Message</div>
  <div class="submit">SUBMIT</div>
</form>

<!-- Services -->
<h2 class="section-title" style="top:896px">Our Services</h2>

<div class="service" style="left:136px;top:1002px">
  <div class="icon"><svg width="40" height="48" viewBox="0 0 40 48"><path d="M2 2h24l12 12v32H2z" fill="var(--brand)"/><path d="M26 2v12h12" fill="#d7ebb0"/><path d="M10 24h20M10 31h20M10 38h14" stroke="#fff" stroke-width="3"/></svg></div>
  <h4>Dolorem Ipsum</h4>
  <p>It is a long established fact that a reader will be distracted by the readable content</p>
</div>
<div class="service" style="left:452px;top:1002px">
  <div class="icon"><svg width="50" height="44" viewBox="0 0 50 44"><rect x="2" y="2" width="46" height="30" rx="3" fill="var(--brand)"/><rect x="7" y="7" width="36" height="20" fill="#fff"/><path d="M20 32h10l3 8H17z" fill="var(--brand)"/><rect x="13" y="39" width="24" height="4" rx="2" fill="var(--brand)"/></svg></div>
  <h4>Porro quisquam</h4>
  <p>It is a long established fact that a reader will be distracted by the readable content</p>
</div>
<div class="service" style="left:767px;top:1002px">
  <div class="icon"><svg width="44" height="44" viewBox="0 0 44 44"><path d="M2 2h32l8 8v32H2z" fill="none" stroke="var(--brand)" stroke-width="4"/><rect x="10" y="4" width="20" height="11" fill="var(--brand)"/><rect x="9" y="24" width="26" height="16" fill="none" stroke="var(--brand)" stroke-width="3"/></svg></div>
  <h4 style="margin-top:48px">Neque porro</h4>
  <p>It is a long established fact that a reader will be distracted by the readable content</p>
</div>

<!-- About -->
<div class="about-band"></div>
<svg class="abs" style="left:0;top:1405px" width="520" height="436" viewBox="0 0 520 436" role="img" aria-label="Photo of business people working on a laptop showing financial charts">
  <defs>
    <linearGradient id="aboutShade" x1="0" y1="0" x2="1" y2="1">
      <stop offset="0" stop-color="#b9c3cc"/>
      <stop offset=".5" stop-color="#5d6f82"/>
      <stop offset="1" stop-color="#2d3c4d"/>
    </linearGradient>
  </defs>
  <path d="M0 0H500C470 150 430 320 440 436H0Z" fill="url(#aboutShade)"/>
  <path d="M500 0C470 150 430 320 440 436" fill="none" stroke="var(--green)" stroke-width="8"/>
</svg>
<div class="about-kicker">About us</div>
<h2 class="about-title">Porro quisquam est qui dolorem ipsum</h2>
<p class="about-text">The point of using Lorem Ipsum is that it has a more-or-less normal distribution of letters, as opposed to using 'Content here, content here', making it look like readable English. Many desktop publishing packages and web page editors now use Lorem Ipsum as their default model text, and a search: The point of using Lorem Ipsum is that it has a more-or-less normal distribution of letters, as opposed to using 'Content here, content here',</p>
<div class="pill-btn" style="left:603px;top:1750px;width:100px">Read More</div>

<!-- Who we are -->
<h2 class="section-title" style="top:1971px">Who We Are</h2>

<article class="team-card" style="left:106px">
  <div class="photo" role="img" aria-label="Photo of stacked coins" style="background:linear-gradient(135deg,#9eb3c4,#3e5468 60%,#1f2c38)"></div>
  <h4>Neque porro quisquam</h4>
  <p>The point of using Lorem Ipsum is that it has a more-or-less normal distribution</p>
  <div class="more">Read More »</div>
</article>
<article class="team-card" style="left:445px">
  <div class="photo" role="img" aria-label="Photo of a hand holding a rising bar chart" style="background:linear-gradient(135deg,#e8eef3,#9fb7cc 55%,#4b6e93)"></div>
  <h4>Porro quisquam est</h4>
  <p>The point of using Lorem Ipsum is that it has a more-or-less normal distribution</p>
  <div class="more">Read More »</div>
</article>
<article class="team-card" style="left:783px">
  <div class="photo" role="img" aria-label="Photo of a desk with a laptop and printed charts" style="background:linear-gradient(135deg,#c9b7a6,#e8e2dc 50%,#8a6d5a)"></div>
  <h4>Dolorem ipsum quia</h4>
  <p>The point of using Lorem Ipsum is that it has a more-or-less normal distribution</p>
  <div class="more">Read More »</div>
</article>

<!-- Statistics -->
<section class="stats">
  <h2>Statistic</h2>
  <div class="stat" style="left:77px"><b>725M</b><span>Quisquam</span></div>
  <div class="stat" style="left:348px"><b>700M</b><span>Dolorem</span></div>
  <div class="stat" style="left:617px"><b>10M+</b><span>Consectetur</span></div>
  <div class="stat" style="left:885px"><b>600M</b><span>Quisquam</span></div>
</section>

<!-- Blog -->
<h2 class="section-title" style="top:3040px">Latest Blog</h2>

<article class="blog-card" style="left:91px" role="img" aria-label="Photo of a businessman looking at glowing financial charts">
  <div style="position:absolute;inset:0;background:linear-gradient(120deg,#6d8aa3,#3a4d62 45%,#8a3b33 75%,#2a3a52)"></div>
  <div class="blog-caption"><h4>Lorem ipsum dolor amet</h4><span>12/02/2018</span></div>
</article>
<article class="blog-card" style="left:613px" role="img" aria-label="Photo of a businessman drawing a rising arrow over a city skyline">
  <div style="position:absolute;inset:0;background:linear-gradient(120deg,#d9dde1,#a7afb8 45%,#2b2f36 75%,#e4e6e8)"></div>
  <div class="blog-caption"><h4>Ipsum dolor amet magna</h4><span>13/02/2018</span></div>
</article>
<a class="view-more">View more</a>

<!-- Footer -->
<svg class="footer" viewBox="0 0 1200 297" preserveAspectRatio="none">
  <path d="M0 70 C 400 10 800 0 1200 10 L1200 297 L0 297Z" fill="var(--green)"/>
  <path d="M0 70 C 400 30 800 40 1200 70 L1200 297 L0 297Z" fill="var(--footer)"/>
</svg>
<div class="footer-name">KTW Ledgerwise Office Services Pty Ltd</div>
<div class="socials"><i></i><i></i><i></i><i></i><i></i></div>
<div class="copyright">Copyright © 2018 All Rights Reserved</div>

</body>
</html>
```